Accountancy firm needs clean and simple website and optional logo

We need a logo and basic wordpress website design for a Sydney based accountancy firm.
We need a clean and simple logo and website, based on the accounting/finance/tax industry. Simple, credible and official colors.
The logo is expected to be so simple that we have combined into the one job.
If you submit a logo design and we choose it along with someone else's website design you will be paid a bonus of $60. The website design will still win the competition as per normal.
Current website is old and terrible but gives you an idea of the sitemap (super simple) and what they do: www.helmwick.com.au
We want original different to normal template looking designs.
We like videos, and like http://www.marbeckers.com.au/
Feel free to go to reelmoss and use some videos from there.
We are based in Sydney Australia and in the field of taxation and accounting
We want a clean, formal, credible site, limited pages.
The project is guaranteed, so go for it.
Dorrit & Associates
1 page

```html
<!DOCTYPE html>
<html lang="en">
<head>
<meta charset="utf-8">
<title>Dorrit &amp; Associates — Tax Accountants</title>
<link href="https://fonts.googleapis.com/css2?family=Roboto:wght@300;400;500;700&display=swap" rel="stylesheet">
<style>
:root{
  --hero-top:#5f80a8;
  --hero-mid:#6b8cb4;
  --hero-water:#3f6596;
  --white:#ffffff;
  --ink:#1c1c1c;
  --muted:#555c63;
  --accent:#2a9ad6;
  --green:#3cae4e;
  --card:#f5f6f8;
  --card-line:#e9ebee;
  --footer:#262626;
  --footer-bar:#1f1f1f;
  --footer-text:#8b8b8b;
}
*{margin:0;padding:0;box-sizing:border-box}
html,body{width:869px;height:1200px;overflow:hidden}
body{font-family:'Roboto',Arial,sans-serif;background:var(--white);position:relative;color:var(--ink)}
.abs{position:absolute}

.hero{left:0;top:0;width:869px;height:521px;
  background:linear-gradient(180deg,var(--hero-top) 0%,var(--hero-mid) 45%,#7f9cc0 70%,var(--hero-water) 78%,#2f558a 100%)}
.brand{left:70px;top:23px;display:flex;align-items:flex-end;gap:8px;color:var(--white)}
.brand-square{width:61px;height:60px;background:var(--white)}
.brand-text{font-size:11px;font-weight:700;line-height:12px;padding-bottom:1px}
.brand-text span{display:block;font-weight:400;font-size:11.5px}
.nav{top:57px;display:flex;gap:44px;left:424px;font-size:10px;font-weight:500;color:var(--white);letter-spacing:.2px}
.call{left:660px;top:47px;display:flex;align-items:center;color:var(--white)}
.call-divider{width:1px;height:27px;background:rgba(255,255,255,.6);margin:0 16px 0 14px}
.call-label{font-size:7.5px;font-weight:500}
.call-number{font-size:15px;font-weight:400;margin-top:1px}
.hero-title{left:0;width:869px;top:248px;text-align:center;color:var(--white);font-size:24px;font-weight:700;letter-spacing:.2px}
.hero-sub{left:180px;width:509px;top:285px;text-align:center;color:var(--white);font-size:10.5px;line-height:16px}
.hero-btn{left:358px;top:329px;width:151px;height:39px;border:2px solid var(--white);border-radius:20px;color:var(--white);font-size:16px;font-weight:500;display:flex;align-items:center;justify-content:center}

.welcome-kicker{left:0;width:869px;top:572px;text-align:center;font-size:10px;font-weight:500;letter-spacing:1.2px;color:#333}
.welcome-title{left:0;width:869px;top:585px;text-align:center;font-size:24px;font-weight:500;color:var(--ink)}
.welcome-rule{left:418px;top:623px;width:33px;height:2px;background:var(--green)}
.welcome-copy{left:190px;width:489px;top:639px;text-align:center;font-size:9px;line-height:16px;color:var(--muted);font-weight:300}

.card{top:703px;width:197px;height:202px;background:var(--card);border:1px solid var(--card-line);border-radius:3px;text-align:center}
.card svg{margin-top:32px}
.card-title{font-size:8.5px;font-weight:500;letter-spacing:.8px;margin-top:10px;color:#333}
.card-list{list-style:none;font-size:9px;line-height:16px;color:var(--muted);margin-top:14px}
.card-link{display:inline-block;margin-top:5px;font-size:9.5px;color:var(--accent)}

.footer{left:0;top:976px;width:869px;height:178px;background:var(--footer)}
.footer-head{font-size:10px;font-weight:500;color:var(--white)}
.field{left:71px;width:267px;height:21px;background:var(--white);border-radius:5px;font-size:7px;color:#999;padding:7px 9px}
.send{left:73px;top:1094px;width:61px;height:20px;background:var(--accent);border-radius:10px;color:var(--white);font-size:8.5px;font-weight:500;display:flex;align-items:center;justify-content:center}
.addr{font-size:7.5px;line-height:14px;color:var(--footer-text)}
.addr b{font-weight:400;color:var(--accent)}
.sitemap{list-style:none;font-size:7.5px;color:var(--footer-text)}
.sitemap li{height:18.5px;display:flex;align-items:flex-start;gap:8px}
.bar{left:0;top:1154px;width:869px;height:46px;background:var(--footer-bar)}
.copyright{left:71px;top:1174px;font-size:7.5px;color:var(--footer-text)}
.social{left:718px;top:1173px;display:flex;gap:14px}
.social span{width:11px;height:11px;border-radius:50%;background:#9aa0a6}
</style>
</head>
<body>

<div class="abs hero" role="img" aria-label="Photo of Sydney harbour with the city skyline and opera house under a blue overlay"></div>

<div class="abs brand">
  <div class="brand-square"></div>
  <div class="brand-text">DORRIT &amp; ASSOCIATES<span>tax accountants</span></div>
</div>

<nav class="abs nav"><span>HOME</span><span>ABOUT</span><span>CONTACT</span></nav>

<div class="abs call">
  <svg width="14" height="26" viewBox="0 0 14 26" fill="none" stroke="#fff" stroke-width="1.2"><rect x="1" y="1" width="12" height="24" rx="2"/><line x1="1" y1="5" x2="13" y2="5"/><line x1="1" y1="20" x2="13" y2="20"/><line x1="5.5" y1="22.5" x2="8.5" y2="22.5"/></svg>
  <div class="call-divider"></div>
  <div><div class="call-label">CALL US NOW FOR</div><div class="call-number">02 7415 2200</div></div>
</div>

<h1 class="abs hero-title">TAKE THE WORRY OUT OF TAX AND BUSINESS</h1>
<p class="abs hero-sub">We collect aggregate information on what pages users or visit and information volunteered by the users such as specific requests to be added to our mailing list.</p>
<div class="abs hero-btn">GET STARTED</div>

<div class="abs welcome-kicker">WELCOME TO</div>
<h2 class="abs welcome-title">DORRIT &amp; ASSOCIATES</h2>
<div class="abs welcome-rule"></div>
<p class="abs welcome-copy">Lorem Ipsum is simply dummy text of the printing and typesetting industry. Lorem Ipsum has been the industry's standard dummy text ever since the 1500s, when an unknown printer</p>

<section class="abs card" style="left:110px">
  <svg width="34" height="34" viewBox="0 0 34 34" fill="none" stroke="#333" stroke-width="1.4"><path d="M4 2h18v16M4 2v30h14"/><line x1="8" y1="8" x2="18" y2="8"/><line x1="8" y1="13" x2="18" y2="13"/><line x1="8" y1="18" x2="14" y2="18"/><circle cx="24" cy="25" r="7"/><line x1="21" y1="28" x2="27" y2="22"/></svg>
  <div class="card-title">TAXES</div>
  <ul class="card-list"><li>Tax Planning and Returns</li><li>Residential loans and financing</li><li>Superannuation self-managed</li></ul>
  <span class="card-link">Click to see more &nbsp;→</span>
</section>

<section class="abs card" style="left:336px">
  <svg width="34" height="34" viewBox="0 0 34 34" fill="none" stroke="#333" stroke-width="1.4"><path d="M6 20l6-3h8l6 4v8H12l-6-4z"/><rect x="14" y="3" width="10" height="13" transform="rotate(15 19 9)"/><line x1="17" y1="9" x2="22" y2="10"/></svg>
  <div class="card-title">ACCOUNTING</div>
  <ul class="card-list"><li>GST preparation and lodgement</li><li>Non resident companies and trusts</li><li>Business Setup</li></ul>
  <span class="card-link">Click to see more &nbsp;→</span>
</section>

<section class="abs card" style="left:561px">
  <svg width="34" height="34" viewBox="0 0 34 34" fill="none" stroke="#333" stroke-width="1.4"><rect x="3" y="2" width="22" height="28" rx="2"/><circle cx="14" cy="10" r="4"/><polyline points="7,22 12,17 16,20 21,15"/><path d="M22 20l6 4v7h-8l-3-4z"/></svg>
  <div class="card-title">ADMINISTRATION</div>
  <ul class="card-list"><li>Litigation assistance</li><li>Business Advisory Services</li><li>Asset Protection Services</li></ul>
  <span class="card-link">Click to see more &nbsp;→</span>
</section>

<footer class="abs footer"></footer>

<div class="abs footer-head" style="left:70px;top:1006px">CONTACT US</div>
<div class="abs field" style="top:1036px">Name</div>
<div class="abs field" style="top:1065px">Email Address</div>
<div class="abs send">SEND</div>

<div class="abs footer-head" style="left:405px;top:1006px">ADDRESS DETAILS</div>
<svg class="abs" style="left:409px;top:1033px" width="8" height="11" viewBox="0 0 8 11"><path d="M4 0a4 4 0 0 1 4 4c0 3-4 7-4 7S0 7 0 4a4 4 0 0 1 4-4z" fill="#fff"/><circle cx="4" cy="4" r="1.5" fill="#262626"/></svg>
<div class="abs addr" style="left:429px;top:1032px">ABN 48 901 552 317<br>Suite G02, 140 Ferrow St<br>Carrow Junction, NSW 2031</div>
<svg class="abs" style="left:409px;top:1089px" width="9" height="9" viewBox="0 0 9 9"><path d="M1 1l2-1 1.5 2.5-1 1a5 5 0 0 0 2 2l1-1L9 6l-1 2C4 8 1 5 1 1z" fill="#fff"/></svg>
<svg class="abs" style="left:409px;top:1103px" width="10" height="9" viewBox="0 0 10 9" fill="#fff"><rect x="2" y="0" width="6" height="3"/><rect x="0" y="3" width="10" height="4" rx="1"/><rect x="2" y="6" width="6" height="3" fill="#262626" stroke="#fff"/></svg>
<div class="abs addr" style="left:429px;top:1087px">Phone: <b>+61 (2) 7415 2200</b><br>Fax: <b>+61 (2) 7415 2299</b></div>

<div class="abs footer-head" style="left:599px;top:1006px">SITE MAP</div>
<ul class="abs sitemap" style="left:600px;top:1036px"><li>→ <span>Home</span></li><li>→ <span>About</span></li><li>→ <span>Contact</span></li><li>→ <span>Services</span></li><li>→ <span>Privacy Policy</span></li></ul>
<ul class="abs sitemap" style="left:715px;top:1036px"><li>→ <span>Careers</span></li><li>→ <span>Available Schedules</span></li></ul>

<div class="abs bar"></div>
<div class="abs copyright">Copyright ©2015 Dorrit &amp; Associates.</div>
<div class="abs social" aria-label="Social links"><span></span><span></span><span></span><span></span></div>

</body>
</html>
```